Custom Home Builder Needs a Website

Harbor Pine Builders Ltd. requires a clean professional 5 page website - Home, About Us, Gallery (Interior and Exterior), Our Process and Contact Us(with registration form). We are a home builder who also has homes for sale. Also please have a place for video embedding. Editable fields by user. Using the stationery 'feel' that is attached. Need social media links. If you require any additional files, please request.

Target Market(s)

Families and professionals

Industry/Entity Type

Home Builder

Coding

Coded - Design and coding required

Number of Pages Required

5+ page

Font styles to use
Sans Serif
Other font styles liked:
• Lato

Requirements
Must have
• Editable by user
• Register Button
• Place to put home models for sale - preferably on the first page
• 5 page website -
• -Home
• -About Us
• -Gallery (Interior and Exterior)
• -Our Process
• -Contact Us.
Nice to have
• Themed similar to current stationery
• place for video embedding
• Try some darker backgrounds
• Change pictures to B/W if works for design
Should not have
• cartoonish type of content

```html
<!DOCTYPE html>
<html lang="en">
<head>
<meta charset="utf-8">
<title>Harbor Pine Builders Ltd.</title>
<link rel="stylesheet" href="https://fonts.googleapis.com/css2?family=Lato:wght@400;700;900&family=Dancing+Script:wght@400;700&display=swap">
<style>
:root{
  --green-dark:#1f4a10;
  --green:#3f8d1b;
  --green-mid:#5aa62a;
  --green-light:#7cbf45;
  --green-pale:#eaf4dc;
  --ink:#222;
  --text:#555;
  --line:#8cc060;
  --white:#fff;
}
*{box-sizing:border-box;margin:0;padding:0}
html,body{width:1200px;height:3249px;overflow:hidden}
body{position:relative;background:var(--white);font-family:'Lato',sans-serif;color:var(--text)}
.abs{position:absolute}

/* header */
.brand-panel{left:0;top:0;width:470px;height:134px;background:var(--green-pale);clip-path:polygon(0 0,100% 0,88% 100%,0 100%)}
.brand{left:70px;top:38px;display:flex;align-items:center;gap:14px}
.brand-square{width:40px;height:40px;background:var(--green)}
.brand-name{font-size:25px;font-weight:900;color:var(--green-dark);letter-spacing:.5px;line-height:1}
.topbar{left:540px;top:0;width:660px;height:39px;background:var(--green);clip-path:polygon(0 0,100% 0,100% 100%,0 100%)}
.topbar-back{left:420px;top:0;width:120px;height:134px;background:var(--green-mid);clip-path:polygon(100% 0,100% 28%,20% 100%,0 100%)}
.phone{left:545px;top:8px;color:var(--white);font-size:17px;display:flex;align-items:center;gap:8px}
.social{right:40px;top:9px;display:flex;gap:14px}
.social span{width:20px;height:20px;border-radius:50%;border:2px solid rgba(255,255,255,.85)}
.nav{left:505px;top:39px;width:695px;height:52px;background:var(--green-light);clip-path:polygon(7% 0,100% 0,100% 100%,0 100%)}
.nav ul{list-style:none;display:flex;gap:38px;position:absolute;left:63px;top:15px}
.nav a{color:var(--white);text-decoration:none;font-size:18px}
.header-rule{left:0;top:130px;width:1200px;border-top:2px dashed var(--line)}

/* hero */
.hero{left:0;top:134px;width:1200px;height:570px;background:linear-gradient(180deg,#8fb8dc 0%,#c9dbe8 35%,#6a6f72 60%,#4c5a44 85%,#6f8f44 100%)}
.hero-banner{left:693px;top:559px;width:507px;height:145px;background:rgba(70,150,30,.9);clip-path:polygon(9% 0,100% 0,100% 100%,0 100%)}
.hero-title{right:42px;top:570px;text-align:right;color:var(--white);font-family:'Dancing Script',cursive;line-height:1.05}
.hero-title .big{font-size:58px;display:block}
.hero-title .sub{font-size:40px;display:block}

/* dividers */
.divider{left:0;width:1200px;border-top:2px dashed var(--line)}
.divider-icon{width:58px;height:58px;border-radius:50%;background:var(--white);border:2px solid var(--line);left:571px;display:flex;align-items:center;justify-content:center}

/* headings */
.eyebrow{font-family:'Dancing Script',cursive;font-size:17px;color:var(--ink);text-align:center;width:100%}
.section-title{font-size:39px;font-weight:700;color:var(--ink);text-align:center;width:100%}
.section-title em{font-style:normal;color:var(--green)}

/* about */
.about-eyebrow{left:78px;top:768px;width:615px}
.about-title{left:78px;top:788px;width:615px}
.about-text{left:78px;top:853px;width:615px;font-size:15.5px;line-height:1.55;text-align:center}
.btn{background:var(--green-dark);color:var(--white);font-size:19px;display:flex;align-items:center;justify-content:center;border-radius:3px}
.about-btn{left:301px;top:970px;width:157px;height:46px}
.video{left:715px;top:773px;width:407px;height:241px;background:linear-gradient(180deg,#b8c4c9,#5e6b5a 70%,#7d8a6c)}
.play{left:890px;top:856px;width:80px;height:80px;border-radius:50%;border:3px solid rgba(255,255,255,.8);background:rgba(255,255,255,.25)}

/* recently added */
.cards{left:78px;top:1256px;width:1044px;height:184px}
.card{position:absolute;top:0;height:184px}
.card-feature{left:0;width:249px;background:linear-gradient(180deg,#3d7a25,#2b5c19);color:var(--white);text-align:center;border:2px solid #6aa43e}
.card-feature h3{font-size:19px;font-weight:400;margin-top:38px}
.card-feature p{font-size:14.5px;margin:14px 18px 0;line-height:1.35}
.card-feature .book{display:inline-block;margin-top:14px;border:1px solid var(--white);padding:7px 28px;font-size:15px}
.card-photo{background:linear-gradient(180deg,#c7d4de,#5b5f5a 55%,#8b8e84)}
.card-sep{position:absolute;top:0;width:1px;height:216px;background:#ddd}
.cards-rule{left:78px;top:1499px;width:1044px;border-top:1px solid #ccc}
.more-btn{left:522px;top:1523px;width:156px;height:45px}

/* process */
.step{top:1800px;width:310px;height:162px}
.step svg{position:absolute;left:0;top:0}
.step h4{position:absolute;left:104px;top:50px;font-size:22px;color:var(--ink);font-weight:700}
.step p{position:absolute;left:104px;top:82px;font-size:15px;color:var(--green);line-height:1.35;width:200px}
.chev{top:1866px}

/* testimonial */
.quote-box{left:156px;top:2205px;width:888px;height:139px;border:2px solid var(--green-mid)}
.quote-side{position:absolute;top:0;width:70px;height:100%;display:flex;align-items:center;justify-content:center}
.quote-side.left{left:0;border-right:1px solid var(--green-mid)}
.quote-side.right{right:0;border-left:1px solid var(--green-mid)}
.quote-text{position:absolute;left:100px;right:100px;top:28px;text-align:center;font-size:15.5px;line-height:1.5}
.quote-rule{position:absolute;left:200px;right:200px;top:80px;border-top:1px solid #999}
.quote-name{position:absolute;left:0;right:0;top:93px;text-align:center;font-weight:700;color:var(--ink);font-size:16px}

/* gallery */
.tile{position:absolute}

/* footer */
.contact{top:3093px;display:flex;align-items:center;gap:22px}
.contact-box{width:44px;height:44px;border:1px solid #ccc;display:flex;align-items:center;justify-content:center}
.contact span{font-size:14.5px;line-height:1.6;color:#666}
.copyright{left:0;top:3195px;width:1200px;height:54px;background:var(--green-dark);color:var(--white);font-size:16px;display:flex;align-items:center;justify-content:center}
.copyright b{color:var(--green-light);font-weight:400;margin:0 4px}
</style>
</head>
<body>

<header>
  <div class="abs topbar-back"></div>
  <div class="abs brand-panel"></div>
  <div class="abs brand"><div class="brand-square"></div><div class="brand-name">HARBOR PINE<br>BUILDERS LTD.</div></div>
  <div class="abs topbar"></div>
  <div class="abs phone">
    <svg width="18" height="18" viewBox="0 0 24 24"><path d="M6.6 10.8a15 15 0 006.6 6.6l2.2-2.2c.3-.3.7-.4 1-.2 1.1.4 2.3.6 3.6.6.6 0 1 .4 1 1V20c0 .6-.4 1-1 1A17 17 0 013 4c0-.6.4-1 1-1h3.5c.6 0 1 .4 1 1 0 1.3.2 2.5.6 3.6.1.3 0 .7-.2 1z" fill="#fff"/></svg>
    555 014 2278
  </div>
  <div class="abs social" aria-label="Social links"><span></span><span></span><span></span><span></span><span></span><span></span></div>
  <nav class="abs nav"><ul><li><a href="#">Home</a></li><li><a href="#">About Us</a></li><li><a href="#">Gallery</a></li><li><a href="#">Our Process</a></li><li><a href="#">Contact Us</a></li></ul></nav>
  <div class="abs header-rule"></div>
</header>

<section>
  <div class="abs hero" role="img" aria-label="Photo of a two-storey grey family home with double garage and stone columns"></div>
  <div class="abs hero-banner"></div>
  <div class="abs hero-title"><span class="big">LARGEST</span><span class="sub">HARBOR PINE BUILDERS</span></div>
  <div class="abs divider-icon" style="top:681px;background:var(--green-mid);border-color:var(--white)">
    <svg width="20" height="26" viewBox="0 0 10 14"><circle cx="5" cy="2" r="1.6" fill="#fff"/><rect x="3.6" y="5" width="2.8" height="8" fill="#fff"/></svg>
  </div>
</section>

<section>
  <div class="abs about-eyebrow eyebrow">Who We Are?</div>
  <h2 class="abs about-title section-title">About <em>Harbor Pine Builders</em></h2>
  <p class="abs about-text">Lorem Ipsum is simply dummy text of the printing and typesetting industry. Lorem Ipsum has been the industry's standard dummy text ever since the 1500s, when an unknown printer took a galley of type and scrambled it to make a type specimen book.</p>
  <div class="abs btn about-btn">READ MORE</div>
  <div class="abs video" role="img" aria-label="Video placeholder showing a grey family home exterior"></div>
  <div class="abs play"><svg width="74" height="74" viewBox="0 0 74 74"><path d="M30 24l22 13-22 13z" fill="rgba(255,255,255,.85)"/></svg></div>
</section>

<div class="abs divider" style="top:1066px"></div>
<div class="abs divider-icon" style="top:1037px"><svg width="26" height="24" viewBox="0 0 24 22"><path d="M12 2L2 11h3v9h5v-6h4v6h5v-9h3z" fill="var(--green)"/></svg></div>

<section>
  <div class="abs eyebrow" style="top:1144px;left:0">Featured Property</div>
  <h2 class="abs section-title" style="top:1163px;left:0">Recently <em>Added</em></h2>
  <div class="abs cards">
    <div class="card card-feature"><h3>Lorem Ipsum dummy</h3><p>Lorem Ipsum has been the industry's standard...</p><span class="book">BOOK NOW</span></div>
    <div class="card-sep" style="left:255px"></div>
    <div class="card card-photo" style="left:262px;width:251px" role="img" aria-label="Photo of a craftsman-style home with garage"></div>
    <div class="card-sep" style="left:520px"></div>
    <div class="card card-photo" style="left:528px;width:252px" role="img" aria-label="Photo of a dark grey two-storey home"></div>
    <div class="card-sep" style="left:787px"></div>
    <div class="card card-photo" style="left:795px;width:249px" role="img" aria-label="Photo of a grey home with gabled roof"></div>
  </div>
  <div class="abs cards-rule"></div>
  <div class="abs btn more-btn">VIEW MORE</div>
</section>

<div class="abs divider" style="top:1640px"></div>
<div class="abs divider-icon" style="top:1611px"><svg width="26" height="26" viewBox="0 0 24 24"><circle cx="12" cy="12" r="7" fill="none" stroke="var(--green)" stroke-width="4" stroke-dasharray="3 2.5"/><circle cx="12" cy="12" r="2.5" fill="var(--green)"/></svg></div>

<section>
  <div class="abs eyebrow" style="top:1715px;left:0">How we Work?</div>
  <h2 class="abs section-title" style="top:1735px;left:0">Working <em>Process</em></h2>

  <div class="abs step" style="left:113px">
    <svg width="170" height="162" viewBox="0 0 170 162"><path d="M148 44A78 78 0 1 0 148 118" fill="none" stroke="var(--green)" stroke-width="6"/><rect x="28" y="66" width="30" height="22" fill="none" stroke="var(--green-light)" stroke-width="4"/><circle cx="34" cy="94" r="5" fill="#444"/><circle cx="54" cy="94" r="5" fill="#444"/></svg>
    <h4>Step 1</h4><p>Lorem Ipsum has been the industry's standard.</p>
  </div>
  <svg class="abs chev" style="left:412px" width="26" height="28" viewBox="0 0 26 28"><path d="M4 2l16 12L4 26" fill="none" stroke="var(--green-light)" stroke-width="6"/></svg>
  <div class="abs step" style="left:466px">
    <svg width="170" height="162" viewBox="0 0 170 162"><path d="M148 44A78 78 0 1 0 148 118" fill="none" stroke="var(--green)" stroke-width="6"/><circle cx="44" cy="80" r="17" fill="none" stroke="#444" stroke-width="5"/><circle cx="58" cy="94" r="10" fill="var(--green-light)"/></svg>
    <h4>Step 2</h4><p>Lorem Ipsum has been the industry's standard.</p>
  </div>
  <svg class="abs chev" style="left:765px" width="26" height="28" viewBox="0 0 26 28"><path d="M4 2l16 12L4 26" fill="none" stroke="var(--green-light)" stroke-width="6"/></svg>
  <div class="abs step" style="left:819px">
    <svg width="170" height="162" viewBox="0 0 170 162"><path d="M148 44A78 78 0 1 0 148 118" fill="none" stroke="var(--green)" stroke-width="6"/><path d="M24 80l22-18 22 18v18H24z" fill="#444"/><rect x="40" y="84" width="12" height="14" fill="var(--green-light)"/></svg>
    <h4>Step 3</h4><p>Lorem Ipsum has been the industry's standard.</p>
  </div>
</section>

<div class="abs divider" style="top:2038px"></div>
<div class="abs divider-icon" style="top:2009px"><svg width="26" height="20" viewBox="0 0 26 20"><path d="M2 18V10c0-5 3-8 8-9v3c-3 1-4 3-4 5h4v9zM15 18V10c0-5 3-8 8-9v3c-3 1-4 3-4 5h4v9z" fill="none" stroke="var(--green-light)" stroke-width="1.8"/></svg></div>

<section>
  <div class="abs eyebrow" style="top:2118px;left:0">What Our Client's Say?</div>
  <h2 class="abs section-title" style="top:2136px;left:0">Testimonial</h2>
  <div class="abs quote-box">
    <div class="quote-side left"><svg width="22" height="22" viewBox="0 0 22 22"><circle cx="11" cy="11" r="9" fill="none" stroke="var(--green-light)" stroke-width="2"/><path d="M13 6l-5 5 5 5" fill="none" stroke="var(--green-light)" stroke-width="2"/></svg></div>
    <p class="quote-text">"Lorem Ipsum is simply dummy text of the printing and typesetting industry. Lorem Ipsum has been the industry's standard dummy text ever since the 1500s."</p>
    <div class="quote-rule"></div>
    <div class="quote-name">- Elena Marsh</div>
    <div class="quote-side right"><svg width="22" height="22" viewBox="0 0 22 22"><circle cx="11" cy="11" r="9" fill="none" stroke="var(--green-light)" stroke-width="2"/><path d="M9 6l5 5-5 5" fill="none" stroke="var(--green-light)" stroke-width="2"/></svg></div>
  </div>
</section>

<div class="abs divider" style="top:2417px"></div>
<div class="abs divider-icon" style="top:2388px"><svg width="26" height="22" viewBox="0 0 26 22"><rect x="2" y="2" width="22" height="18" fill="none" stroke="var(--green)" stroke-width="2.5"/><path d="M4 18l7-8 5 5 3-3 5 6z" fill="var(--green)"/></svg></div>

<section>
  <div class="abs eyebrow" style="top:2502px;left:0">Our Work</div>
  <h2 class="abs section-title" style="top:2519px;left:0">Our <em>Gallery</em></h2>
  <div class="abs" style="left:78px;top:2586px;width:1044px;height:377px">
    <div class="tile" style="left:0;top:0;width:255px;height:156px;background:linear-gradient(135deg,#e6e8e6,#8a8f86)" role="img" aria-label="Interior photo of a bright home office"></div>
    <div class="tile" style="left:0;top:167px;width:255px;height:210px;background:linear-gradient(180deg,#d4dbde,#6f7470)" role="img" aria-label="Interior photo of a white bathroom vanity"></div>
    <div class="tile" style="left:263px;top:0;width:255px;height:230px;background:linear-gradient(180deg,#c6d3de,#5f6560 60%,#6e8d48)" role="img" aria-label="Exterior photo of a grey two-storey home"></div>
    <div class="tile" style="left:263px;top:239px;width:255px;height:138px;background:linear-gradient(180deg,#c2d0de,#474c48 60%,#6c8c44)" role="img" aria-label="Exterior photo of a dark home with lawn"></div>
    <div class="tile" style="left:528px;top:0;width:254px;height:138px;background:linear-gradient(135deg,#eceae6,#c9b6c2)" role="img" aria-label="Interior photo of a child's bedroom"></div>
    <div class="tile" style="left:528px;top:147px;width:254px;height:230px;background:linear-gradient(180deg,#a79a88,#4a3326)" role="img" aria-label="Interior photo of a kitchen with dark wood cabinets"></div>
    <div class="tile" style="left:790px;top:0;width:254px;height:208px;background:linear-gradient(180deg,#c8d6e0,#5c605b 60%,#6e9048)" role="img" aria-label="Exterior photo of a grey craftsman home"></div>
    <div class="tile" style="left:790px;top:217px;width:254px;height:160px;background:linear-gradient(135deg,#eeeeea,#7e7266)" role="img" aria-label="Interior photo of a white kitchen"></div>
  </div>
</section>

<div class="abs divider" style="top:3039px"></div>
<div class="abs divider-icon" style="top:3010px"><svg width="22" height="28" viewBox="0 0 22 28"><path d="M11 2a8 8 0 00-8 8c0 6 8 16 8 16s8-10 8-16a8 8 0 00-8-8z" fill="var(--green)"/><circle cx="11" cy="10" r="3" fill="#fff"/></svg></div>

<footer>
  <div class="abs contact" style="left:78px">
    <div class="contact-box"><svg width="16" height="20" viewBox="0 0 22 28"><path d="M11 2a8 8 0 00-8 8c0 6 8 16 8 16s8-10 8-16a8 8 0 00-8-8z" fill="none" stroke="#777" stroke-width="2"/></svg></div>
    <span style="text-align:center">123,Lorem Ipsum,Area,<br>City,Country,<br>Zip Code</span>
  </div>
  <div class="abs contact" style="left:503px;top:3103px">
    <div class="contact-box"><svg width="18" height="18" viewBox="0 0 24 24"><path d="M6.6 10.8a15 15 0 006.6 6.6l2.2-2.2c.3-.3.7-.4 1-.2 1.1.4 2.3.6 3.6.6.6 0 1 .4 1 1V20c0 .6-.4 1-1 1A17 17 0 013 4c0-.6.4-1 1-1h3.5c.6 0 1 .4 1 1 0 1.3.2 2.5.6 3.6.1.3 0 .7-.2 1z" fill="none" stroke="#777" stroke-width="1.6"/></svg></div>
    <span>(555) 014 3390</span>
  </div>
  <div class="abs contact" style="left:827px;top:3103px">
    <div class="contact-box"><svg width="20" height="14" viewBox="0 0 20 14"><rect x="1" y="1" width="18" height="12" fill="none" stroke="#777" stroke-width="1.6"/><path d="M1 1l9 7 9-7" fill="none" stroke="#777" stroke-width="1.6"/></svg></div>
    <span>hello@harborpinebuilders.com</span>
  </div>
  <div class="abs copyright">Copyright 2016 ~<b>Harborpinebuilders</b>~All rights reserved.</div>
</footer>

</body>
</html>
```